redesign existing business card

Re design our business cards. We want a modern elegant design, open to ideas front side must contain similar details in a fresh look and style, back side we are open to suggestions. MUST USE COMPANY COLORS, WE WANT BRANDING. Need more ideas see www.brightstoneyards.com - Project must be done in one of adobe products and all files and fonts must be submitted to us. THIS IS A MUST

Target Market(s)

home owners

Industry/Entity Type

Construction Company

Contact Information for Business Card

see existing card file for information

Font styles to use
Sans Serif

Colors
0455a3
3377b5
34a6d7
0592cd
85cae6
ffffff

Requirements
Must have
• company colors, logo, contact info this is all for front side. back side be creative.

```html
<!DOCTYPE html>
<html lang="en">
<head>
<meta charset="utf-8">
<title>Brightstone Yards — Business Card</title>
<link href="https://fonts.googleapis.com/css2?family=Roboto+Condensed:ital,wght@0,300;0,400;0,700;1,700&display=swap" rel="stylesheet">
<style>
  :root {
    --navy: #0455a3;
    --mid-blue: #3377b5;
    --sky: #34a6d7;
    --cerulean: #0592cd;
    --pale: #85cae6;
    --white: #ffffff;
    --card-top: #c9e8f5;
    --card-bottom: #8ccce8;
    --stage: #eef1f4;
  }
  * { margin: 0; padding: 0; box-sizing: border-box; }
  html, body { width: 1200px; height: 892px; overflow: hidden; }
  body {
    background: var(--stage);
    font-family: "Roboto Condensed", sans-serif;
    display: flex;
    flex-direction: column;
    align-items: center;
    justify-content: center;
    gap: 46px;
  }
  .card {
    position: relative;
    width: 620px;
    height: 354px;
    border-radius: 4px;
    overflow: hidden;
    background: linear-gradient(160deg, var(--card-top), var(--card-bottom));
    box-shadow: 0 6px 18px rgba(4, 85, 163, 0.18);
  }
  .card-wave { position: absolute; inset: 0; width: 100%; height: 100%; }

  /* Front */
  .contact {
    position: absolute;
    left: 34px;
    top: 22px;
    color: var(--cerulean);
  }
  .contact-name {
    font-weight: 700;
    font-size: 30px;
    letter-spacing: 0.5px;
    color: var(--cerulean);
    text-transform: uppercase;
    line-height: 1;
  }
  .contact-direct {
    font-size: 19px;
    margin-top: 5px;
    color: var(--cerulean);
  }
  .contact-direct b { font-weight: 700; }
  .contact-label {
    font-size: 10px;
    letter-spacing: 0.5px;
    text-transform: uppercase;
    margin-top: 6px;
    color: var(--mid-blue);
  }
  .contact-line {
    font-size: 15px;
    line-height: 1.2;
    color: var(--cerulean);
  }
  .contact-line.web { color: var(--white); }
  .contact-line.gap { margin-top: 6px; }

  .brand {
    position: absolute;
    right: 34px;
    top: 178px;
    display: flex;
    align-items: center;
    gap: 10px;
    font-weight: 700;
    font-size: 30px;
    color: var(--navy);
    text-transform: uppercase;
    letter-spacing: 1px;
  }
  .brand-mark { width: 18px; height: 18px; background: var(--navy); }

  /* Back */
  .services {
    position: absolute;
    left: 0;
    width: 360px;
    top: 30px;
    text-align: center;
    list-style: none;
    color: var(--navy);
    font-weight: 700;
    font-style: italic;
    font-size: 21px;
    line-height: 1.32;
  }
  .family {
    position: absolute;
    left: 0;
    width: 360px;
    top: 206px;
    text-align: center;
    color: var(--white);
    font-weight: 700;
    font-style: italic;
    font-size: 16px;
  }
  .license {
    position: absolute;
    left: 0;
    width: 380px;
    top: 236px;
    text-align: center;
    color: var(--mid-blue);
    font-weight: 300;
    font-size: 16px;
    line-height: 1.2;
  }
  .brand-faint {
    position: absolute;
    right: 30px;
    top: 190px;
    font-weight: 700;
    font-size: 24px;
    color: var(--mid-blue);
    letter-spacing: 1px;
    text-transform: uppercase;
  }
</style>
</head>
<body>

  <section class="card card-front" aria-label="Business card front">
    <svg class="card-wave" viewBox="0 0 620 354" preserveAspectRatio="none" aria-hidden="true">
      <path d="M0 246 C 110 254, 200 300, 290 326 C 360 344, 420 350, 490 354 L0 354 Z" fill="var(--sky)"/>
      <path d="M0 253 C 110 262, 195 306, 282 331 C 350 347, 405 352, 460 354 L0 354 Z" fill="var(--white)"/>
      <path d="M0 266 C 100 276, 180 316, 262 338 C 310 350, 350 353, 390 354 L0 354 Z" fill="var(--cerulean)" opacity="0.55"/>
      <path d="M0 282 C 90 292, 160 326, 230 343 C 260 350, 285 353, 310 354 L0 354 Z" fill="var(--cerulean)"/>
    </svg>
    <div class="contact">
      <div class="contact-name">Nolan Reyes</div>
      <div class="contact-direct"><b>DIRECT :</b> (555)210-4837</div>
      <div class="contact-label">Office - Showroom</div>
      <div class="contact-line">418 Harbor Crest Way suite 6</div>
      <div class="contact-line">Palm Shore, FL 33900</div>
      <div class="contact-line gap">O : (555)318-2069</div>
      <div class="contact-line">F : (555)318-2070</div>
      <div class="contact-line web gap">www.brightstoneyards.com</div>
      <div class="contact-line web">nolan@brightstoneyards.com</div>
    </div>
    <div class="brand"><span class="brand-mark"></span>Brightstone Yards</div>
  </section>

  <section class="card card-back" aria-label="Business card back">
    <svg class="card-wave" viewBox="0 0 620 354" preserveAspectRatio="none" aria-hidden="true">
      <path d="M0 300 C 150 290, 260 308, 380 322 C 480 334, 560 326, 620 320 L620 354 L0 354 Z" fill="var(--sky)"/>
      <path d="M0 307 C 150 297, 260 314, 380 329 C 480 340, 560 333, 620 327 L620 354 L0 354 Z" fill="var(--white)"/>
      <path d="M0 322 C 150 310, 260 326, 380 340 C 480 350, 560 342, 620 336 L620 354 L0 354 Z" fill="var(--cerulean)"/>
    </svg>
    <ul class="services">
      <li>Driveway</li>
      <li>Pool Renovation</li>
      <li>Custom out-Door Kitchen</li>
      <li>Retaining wall</li>
      <li>h.o.a projects</li>
      <li>Patios &amp; Much More</li>
    </ul>
    <div class="family">Family Owned &amp; Operated</div>
    <div class="license">
      License &amp; Insured<br>
      CTY 24-HS-30417_A SHR CO V-55102<br>
      LAKE LKHDS7718
    </div>
    <div class="brand-faint">Brightstone Yards</div>
  </section>

</body>
</html>
```